Real Estate Renovation and Rental:Business Card/Logo Design Project

Corliss Grove LLC is a small partnership that buys homes to renovate, then provide as rentals to people who may not currently be able to purchase a home - but we also coach them on how to improve their credit so that, in 2-5 years, they may be able to buy a home. Maybe even the one they're living in.

We are based in Sonoma County of Northern California, operating in communities including Healdsburg, Windsor, Santa Rosa, and Cloverdale.

Please design a business card, but the same logo should work for signs that we will post on the homes as they are being renovated.

The design should be clean, contemporary, professional but warm. I'd love to see a rooftop feature, or some other element of a house. Again, not too much detail, clean and welcoming. The design must include "Corliss Grove LLC" - but "CGLLC" could also be used as a primary name, with "Corliss Grove LLC" in smaller print somewhere. If using "CGLLC", the CG could be visually distinct (larger, different color, font) than the LLC part of the name but they must be together.
Updates

just conferring with partner to choose a final design ... should be ready to choose soon and will post

Industry/Entity Type

Business

Requirements
Must have
• the name "Corliss Grove LLC"
for business card design, and leave room for us to customize with partner names, address, telephone numbers, email addresses
Nice to have
• some element of a house included

```html
<!DOCTYPE html>
<html lang="en">
<head>
<meta charset="utf-8">
<title>Corliss Grove LLC — Business Card</title>
<link rel="stylesheet" href="https://fonts.googleapis.com/css2?family=Questrial&display=swap">
<style>
  :root {
    --backdrop: #2b2b2b;
    --brand-orange: #f08a0a;
    --pattern-orange: #ec8106;
    --brand-blue: #2f74c0;
    --card-white: #ffffff;
    --pattern-grey: #f4f4f4;
    --ink: #4a4a4a;
    --rule: #6b6b6b;
  }
  * { box-sizing: border-box; margin: 0; padding: 0; }
  html, body { width: 1200px; height: 900px; overflow: hidden; }
  body {
    background: var(--backdrop);
    font-family: "Questrial", "Century Gothic", sans-serif;
    position: relative;
  }
  .card {
    position: absolute;
    top: 300px;
    width: 540px;
    height: 300px;
    border-radius: 18px;
    overflow: hidden;
    box-shadow: 0 6px 14px rgba(0,0,0,0.45);
  }
  .card--front { left: 45px; background: var(--brand-orange); }
  .card--back { left: 615px; background: var(--card-white); }
  .card__pattern {
    position: absolute; inset: 0;
  }
  .card--front .card__pattern { background: linear-gradient(180deg, var(--brand-orange), var(--pattern-orange)); }
  .card--back .card__pattern { background: linear-gradient(180deg, var(--card-white), var(--pattern-grey)); }

  .lockup { position: absolute; text-align: center; }
  .lockup__mark {
    display: block;
    line-height: 1;
    letter-spacing: 1px;
  }
  .lockup__rule { display: block; height: 2px; margin: 6px 0 4px; }
  .lockup__name { display: block; }

  .card--front .lockup { left: 142px; top: 132px; width: 256px; }
  .card--front .lockup__mark { font-size: 76px; color: var(--card-white); }
  .card--front .lockup__rule { background: var(--rule); }
  .card--front .lockup__name { font-size: 21px; color: var(--brand-blue); }

  .card--back .lockup { left: 46px; top: 132px; width: 184px; }
  .card--back .lockup__mark { font-size: 54px; color: var(--brand-orange); }
  .card--back .lockup__rule { background: var(--rule); height: 1.5px; margin: 4px 0 4px; }
  .card--back .lockup__name { font-size: 15px; color: var(--ink); }

  .divider {
    position: absolute; left: 262px; top: 52px;
    width: 2px; height: 196px; background: var(--brand-blue);
  }
  .contact { position: absolute; left: 292px; top: 62px; color: var(--ink); }
  .contact__person { font-size: 24px; color: var(--brand-orange); line-height: 1.1; }
  .contact__role { font-size: 14.5px; margin-bottom: 24px; }
  .contact__row {
    display: flex; align-items: flex-start; gap: 7px;
    font-size: 14.5px; line-height: 1.1;
  }
  .contact__row + .contact__row { margin-top: 2px; }
  .contact__row--gap { margin-top: 14px !important; }
  .contact__icon { width: 12px; height: 12px; flex: none; margin-top: 2px; }
</style>
</head>
<body>

  <section class="card card--front">
    <div class="card__pattern" role="img" aria-label="Repeating pattern of small house rooftops in orange tones"></div>
    <div class="lockup">
      <span class="lockup__mark">CGLLC</span>
      <span class="lockup__rule"></span>
      <span class="lockup__name">Corliss Grove LLC</span>
    </div>
  </section>

  <section class="card card--back">
    <div class="card__pattern" role="img" aria-label="Faint repeating pattern of small house rooftops in light grey"></div>
    <div class="lockup">
      <span class="lockup__mark">CGLLC</span>
      <span class="lockup__rule"></span>
      <span class="lockup__name">Corliss Grove LLC</span>
    </div>

    <div class="divider"></div>

    <div class="contact">
      <p class="contact__person">Dorian Hallwell</p>
      <p class="contact__role">managing director</p>

      <div class="contact__row">
        <svg class="contact__icon" viewBox="0 0 12 12" aria-hidden="true">
          <path d="M6 0.5a4 4 0 0 0-4 4c0 3 4 7 4 7s4-4 4-7a4 4 0 0 0-4-4z" fill="#f08a0a"/>
          <circle cx="6" cy="4.5" r="1.5" fill="#fff"/>
        </svg>
        <span>48 Orchard Lane<br>Healdsburg, California 95448</span>
      </div>
      <div class="contact__row">
        <svg class="contact__icon" viewBox="0 0 12 12" aria-hidden="true">
          <path d="M3 1l2 2.5-1.2 1.3c.6 1.4 1.8 2.6 3.2 3.2L8.3 6.8 11 9l-1.5 2C5 10.5 1.5 7 1 2.5z" fill="#f08a0a"/>
        </svg>
        <span>707 555 01 42</span>
      </div>
      <div class="contact__row contact__row--gap">
        <svg class="contact__icon" viewBox="0 0 12 12" aria-hidden="true">
          <rect x="1" y="3" width="10" height="7" fill="#2f74c0"/>
          <path d="M1 3l5 4 5-4" fill="none" stroke="#fff" stroke-width="1"/>
        </svg>
        <span>info@cgllc.com</span>
      </div>
      <div class="contact__row">
        <svg class="contact__icon" viewBox="0 0 12 12" aria-hidden="true">
          <circle cx="6" cy="6" r="5" fill="#2f74c0"/>
          <path d="M1 6h10M6 1c-2.5 3-2.5 7 0 10M6 1c2.5 3 2.5 7 0 10" fill="none" stroke="#fff" stroke-width="0.8"/>
        </svg>
        <span>www.cgllc.com</span>
      </div>
    </div>
  </section>

</body>
</html>
```